Health Coach needs a Business Card Design

Need a really modern feminine business card design for a health and lifestyle coach. Needs to use geometric shapes, muted grey/blue/green pastels and black and white - see mood board attached and logo. The client likes black and white, modern, san serif with the use of lines and possibly a shadow leaf as in the mood board. Possibly put the tag line on the back or an icon of the logo. Logo is also attached. An icon of the logo would be great too.

Target Market(s)

Women (some men) aged 30 to 50.

Industry/Entity Type

Business

Contact Information for Business Card

Marla Teveny
e-mail: hello@marlatwell.example
website: marlatwell.example
Phone: +610497258316

The tag line is "A steady path to wellness"

Font styles to use
Sans Serif

Colors
ecf7fb
cfeae6
000000
ffffff
f5f5f5

Requirements
Must have
• Black and white, logo, tag line and details
Nice to have
• Would be nice to incorporate the shadow palm.fern leaves as in the mood board and or geometric lines/shapes - see mood board. Could be either standard rectangle or would be happy with square too.
Should not have
• Flowers or decorations

```html
<!DOCTYPE html>
<html lang="en">
<head>
<meta charset="utf-8">
<title>Marla Teveny – Business Card Presentation</title>
<link href="https://fonts.googleapis.com/css2?family=Montserrat:wght@300;400;500&family=Arimo:wght@400&display=swap" rel="stylesheet">
<style>
  :root {
    --board: #45271a;
    --black: #000000;
    --white: #ffffff;
    --leaf-dark: #5f6f6a;
    --leaf-pale: #d6efeb;
    --blush: #f5dcd1;
    --ink: #111111;
  }
  * { margin: 0; padding: 0; box-sizing: border-box; }
  html, body { width: 1200px; height: 1200px; overflow: hidden; }
  body { background: var(--board); font-family: "Montserrat", sans-serif; position: relative; }

  .card { position: absolute; left: 215px; width: 563px; height: 338px; overflow: hidden; }
  .card--front { top: 60px; background: var(--black); }
  .card--back-frame { top: 422px; background: var(--white); }
  .card--back-stripes { top: 784px; background: var(--blush); }

  .view-label { position: absolute; left: 872px; font-family: "Arimo", sans-serif; font-size: 49px; color: var(--white); }
  .view-label--front { top: 210px; }
  .view-label--back1 { top: 564px; }
  .view-label--back2 { top: 913px; }

  /* front */
  .leaf-shadow--front {
    position: absolute; left: 0; top: 0; width: 563px; height: 338px;
    background: radial-gradient(ellipse 300px 160px at 360px 170px, var(--leaf-dark) 0%, rgba(95,111,106,0.8) 55%, rgba(95,111,106,0) 100%);
  }
  .front-frame {
    position: absolute; left: 119px; top: 64px; width: 332px; height: 185px;
    border: 4px solid var(--white); border-radius: 14px;
    transform: rotate(13.4deg);
  }
  .brand-name {
    position: absolute; left: 60px; width: 500px; top: 124px; text-align: center;
    font-weight: 300; font-size: 30px; color: var(--white); letter-spacing: 1px;
  }
  .brand-tagline {
    position: absolute; left: 60px; width: 500px; top: 180px; text-align: center;
    font-weight: 400; font-size: 12px; color: var(--white); letter-spacing: 3.3px;
  }
  .front-url {
    position: absolute; left: 0; width: 563px; top: 296px; text-align: center;
    font-size: 19px; color: var(--white);
  }

  /* backs */
  .leaf-shadow--back {
    position: absolute; left: 10px; top: 0; width: 553px; height: 338px;
    background: radial-gradient(ellipse 260px 170px at 200px 170px, rgba(214,239,235,0.9) 0%, rgba(214,239,235,0.55) 60%, rgba(214,239,235,0) 100%);
  }
  .frame {
    position: absolute; left: 15px; top: 18px; width: 534px; height: 304px;
    border: 6px solid var(--blush); border-radius: 22px;
  }
  .stripe { position: absolute; top: 0; height: 338px; background: var(--white); }

  .holder-name {
    position: absolute; left: 225px; top: 64px;
    font-weight: 400; font-size: 37px; color: var(--ink); letter-spacing: 0.5px;
  }
  .contact-list { position: absolute; left: 226px; top: 164px; list-style: none; }
  .contact-item {
    display: flex; align-items: center; height: 27px; font-size: 20px; color: var(--ink);
  }
  .contact-item--phone { margin-top: 6px; }
  .contact-icon { width: 18px; height: 18px; margin-right: 4px; }
  .tagline-line {
    position: absolute; right: 32px; top: 289px;
    font-size: 20px; letter-spacing: 4.8px; color: var(--ink);
  }
  .tagline-tab {
    position: absolute; left: 77px; top: 278px; width: 486px; height: 43px;
    background: var(--black); border-top-left-radius: 26px;
  }
  .tagline-line--inverse { color: var(--white); top: 288px; }
</style>
</head>
<body>

  <section class="card card--front" aria-label="Card front">
    <div class="leaf-shadow--front" role="img" aria-label="Grey-green shadow palm leaf illustration"></div>
    <div class="front-frame"></div>
    <div class="brand-name">Marla Teveny</div>
    <div class="brand-tagline">A STEADY PATH TO WELLNESS</div>
    <div class="front-url">www.marlatwell.example</div>
  </section>
  <div class="view-label view-label--front">front</div>

  <section class="card card--back-frame" aria-label="Card back, framed version">
    <div class="leaf-shadow--back" role="img" aria-label="Pale mint shadow palm leaf illustration"></div>
    <div class="frame"></div>
    <div class="holder-name">Marla Teveny</div>
    <ul class="contact-list">
      <li class="contact-item">
        <svg class="contact-icon" viewBox="0 0 18 18"><rect x="1" y="4" width="16" height="11" fill="#111"/><path d="M1 4 L9 10 L17 4" fill="none" stroke="#fff" stroke-width="1.4"/></svg>: hello@marlatwell.example
      </li>
      <li class="contact-item">
        <svg class="contact-icon" viewBox="0 0 18 18"><circle cx="9" cy="9" r="7.5" fill="none" stroke="#111" stroke-width="1.6"/><ellipse cx="9" cy="9" rx="3.3" ry="7.5" fill="none" stroke="#111" stroke-width="1.4"/><path d="M1.5 9 H16.5 M3 5 H15 M3 13 H15" stroke="#111" stroke-width="1.3"/></svg>: www.marlatwell.example
      </li>
      <li class="contact-item contact-item--phone">
        <svg class="contact-icon" viewBox="0 0 18 18"><path d="M13 2 L16 4 L14 6 C11 6 7 10 6.5 13 L4.5 15 L2 13 C3 7 7 3 13 2 Z" fill="#111"/></svg>: +610497258316
      </li>
    </ul>
    <div class="tagline-line">A STEADY PATH TO WELLNESS</div>
  </section>
  <div class="view-label view-label--back1">back 1</div>

  <section class="card card--back-stripes" aria-label="Card back, striped version">
    <div class="stripe" style="left:193px;width:47px"></div>
    <div class="stripe" style="left:340px;width:28px"></div>
    <div class="stripe" style="left:430px;width:17px"></div>
    <div class="stripe" style="left:503px;width:17px"></div>
    <div class="stripe" style="left:548px;width:7px"></div>
    <div class="leaf-shadow--back" role="img" aria-label="Pale mint shadow palm leaf illustration"></div>
    <div class="holder-name">Marla Teveny</div>
    <ul class="contact-list">
      <li class="contact-item">
        <svg class="contact-icon" viewBox="0 0 18 18"><rect x="1" y="4" width="16" height="11" fill="#111"/><path d="M1 4 L9 10 L17 4" fill="none" stroke="#fff" stroke-width="1.4"/></svg>: hello@marlatwell.example
      </li>
      <li class="contact-item">
        <svg class="contact-icon" viewBox="0 0 18 18"><circle cx="9" cy="9" r="7.5" fill="none" stroke="#111" stroke-width="1.6"/><ellipse cx="9" cy="9" rx="3.3" ry="7.5" fill="none" stroke="#111" stroke-width="1.4"/><path d="M1.5 9 H16.5 M3 5 H15 M3 13 H15" stroke="#111" stroke-width="1.3"/></svg>: www.marlatwell.example
      </li>
      <li class="contact-item contact-item--phone">
        <svg class="contact-icon" viewBox="0 0 18 18"><path d="M13 2 L16 4 L14 6 C11 6 7 10 6.5 13 L4.5 15 L2 13 C3 7 7 3 13 2 Z" fill="#111"/></svg>: +610497258316
      </li>
    </ul>
    <div class="tagline-tab"></div>
    <div class="tagline-line tagline-line--inverse">A STEADY PATH TO WELLNESS</div>
  </section>
  <div class="view-label view-label--back2">back 2</div>

</body>
</html>
```